Redesign of business card for Birchline Mechanical

We are looking for a new design for our business cards for Birchline Mechanical. We are a plumbing & HVAC construction company, operating on the West Coast of Canada and USA. Logo attached.
Industry/Entity Type
Construction - Plumbing & HVAC
Contact Information for Business Card
Name, address, phone numbers, email, website address
Look and feel
Each slider illustrates characteristics of the customer's brand and the style your logo design should communicate.

```html
<!DOCTYPE html>
<html lang="en">
<head>
<meta charset="utf-8">
<title>Birchline Mechanical — Business Card</title>
<link rel="stylesheet" href="https://fonts.googleapis.com/css2?family=Oswald:wght@500&family=Jost:wght@400&display=swap">
<style>
  :root {
    --backdrop: #6e6e6e;
    --card: #000000;
    --ink: #ffffff;
  }
  * { margin: 0; padding: 0; box-sizing: border-box; }
  html, body {
    width: 1200px;
    height: 1200px;
    overflow: hidden;
    background: var(--backdrop);
  }
  .canvas {
    position: relative;
    width: 1200px;
    height: 1200px;
  }
  .card {
    position: absolute;
    left: 150px;
    width: 898px;
    height: 523px;
    background: var(--card);
    color: var(--ink);
    overflow: hidden;
  }
  .card--front { top: 56px; }
  .card--back { top: 621px; }

  .wordmark {
    position: absolute;
    display: flex;
    align-items: center;
    gap: 18px;
    font-family: "Oswald", "Arial Narrow", sans-serif;
    font-weight: 500;
    text-transform: uppercase;
    color: var(--ink);
    letter-spacing: 0.02em;
    line-height: 1.05;
  }
  .wordmark__square {
    flex: none;
    background: var(--ink);
  }
  .card--front .wordmark {
    left: 90px;
    top: 120px;
    font-size: 48px;
  }
  .card--front .wordmark__square { width: 38px; height: 38px; }
  .card--back .wordmark {
    left: 0;
    right: 0;
    top: 215px;
    justify-content: center;
    font-size: 66px;
  }
  .card--back .wordmark__square { width: 52px; height: 52px; }

  .contact-list {
    position: absolute;
    left: 568px;
    top: 114px;
    list-style: none;
    font-family: "Jost", "Futura", sans-serif;
    font-size: 22px;
    color: var(--ink);
  }
  .contact-list li {
    display: flex;
    align-items: center;
    height: 42px;
  }
  .contact-list svg,
  .address svg {
    width: 20px;
    height: 20px;
    fill: var(--ink);
    flex: none;
    margin-right: 18px;
  }
  .address {
    position: absolute;
    left: 96px;
    top: 416px;
    display: flex;
    align-items: center;
    font-family: "Jost", "Futura", sans-serif;
    font-size: 22px;
  }
  .address svg { margin-right: 20px; }
  .accent-bar {
    position: absolute;
    left: 615px;
    right: 0;
    top: 419px;
    height: 22px;
    background: var(--ink);
  }
</style>
</head>
<body>
<main class="canvas">
  <section class="card card--front" aria-label="Card front">
    <div class="wordmark"><span class="wordmark__square"></span><span>Birchline<br>Mechanical</span></div>

    <ul class="contact-list">
      <li>
        <svg viewBox="0 0 24 24" aria-hidden="true"><path d="M6.6 10.8a15.1 15.1 0 0 0 6.6 6.6l2.2-2.2a1 1 0 0 1 1-.25 11.4 11.4 0 0 0 3.6.57 1 1 0 0 1 1 1V20a1 1 0 0 1-1 1A17 17 0 0 1 3 4a1 1 0 0 1 1-1h3.5a1 1 0 0 1 1 1c0 1.25.2 2.45.57 3.57a1 1 0 0 1-.25 1z"/></svg>
        <span>1234 567 890</span>
      </li>
      <li>
        <svg viewBox="0 0 24 24" aria-hidden="true"><path d="M3 5h18a1 1 0 0 1 1 1v12a1 1 0 0 1-1 1H3a1 1 0 0 1-1-1V6a1 1 0 0 1 1-1zm1 2.3V17h16V7.3l-8 5.2z M4.5 7h15L12 11.8z"/></svg>
        <span>info@webmail.com</span>
      </li>
      <li>
        <svg viewBox="0 0 24 24" aria-hidden="true"><path d="M12 2a10 10 0 1 0 0 20 10 10 0 0 0 0-20zm6.9 6h-3a15.6 15.6 0 0 0-1.3-3.9A8 8 0 0 1 18.9 8zM12 4c.8 1.2 1.5 2.5 1.9 4h-3.8c.4-1.5 1.1-2.8 1.9-4zM4.3 14a8 8 0 0 1 0-4h3.4a16 16 0 0 0 0 4zm.8 2h3a15.6 15.6 0 0 0 1.3 3.9A8 8 0 0 1 5.1 16zm3-8h-3a8 8 0 0 1 4.3-3.9A15.6 15.6 0 0 0 8.1 8zM12 20c-.8-1.2-1.5-2.5-1.9-4h3.8c-.4 1.5-1.1 2.8-1.9 4zm2.3-6H9.7a14.5 14.5 0 0 1 0-4h4.6a14.5 14.5 0 0 1 0 4zm.3 5.9a15.6 15.6 0 0 0 1.3-3.9h3a8 8 0 0 1-4.3 3.9zm1.7-5.9a16 16 0 0 0 0-4h3.4a8 8 0 0 1 0 4z"/></svg>
        <span>www.website.com</span>
      </li>
    </ul>

    <div class="address">
      <svg viewBox="0 0 24 24" aria-hidden="true"><path d="M12 2a7 7 0 0 0-7 7c0 5.2 7 13 7 13s7-7.8 7-13a7 7 0 0 0-7-7zm0 9.5A2.5 2.5 0 1 1 12 6.5a2.5 2.5 0 0 1 0 5z"/></svg>
      <span>12/C, Address, Street, Pincode - 221122</span>
    </div>
    <div class="accent-bar"></div>
  </section>

  <section class="card card--back" aria-label="Card back">
    <div class="wordmark"><span class="wordmark__square"></span><span>Birchline<br>Mechanical</span></div>
  </section>
</main>
</body>
</html>
```